Quiet Resolve: How to Feel Worthy, Step Through Fear and Empower Your Truth

Hello! I'm looking for a very professional-looking ebook cover (to be used for hardcopy as well). I'm looking for a design Similar to "Quiet Ember" by Dorian Petchey or Driftlines by Everett Sandholm (Examples included in attachments). I love how these nonfiction design covers have a white background, with attention-grabbing titles and clean, modern font that grabs the viewer's interest.
I've included sketches of my own that will be helpful to understand my vision for the design. I'm imagining the word "INNER" being thin, and either black or dark grey. I'm imagining the word "COURAGE" to be a deep red, like the underline in my logo (attached).
I'm not sure exactly if all-caps, or a mix of all-caps title and lowercase subtitle are best. I'll leave that to your professional opinion to feel out what gets the message through best and feels right.
In both of the book cover examples attached, there is great use of a sleek, clean image that exemplifies the message of the book. I am stuck here, not quite sure which image/item would be best there. Feel free to use your professional opinion there too!
Beneath all of the words, I would like the image of a tall, healthy green tree emerging from the clouds. I have been inspired by the view from an airplane window as you pop through the clouds, and would like to convey the same feeling of wonder while demonstrating that it's possible to stay grounding while growing to that level of wonder in your own life (hence the tree). I'd like there NOT to be an airplane wing or window edges in view though.
I am open to other ways to depict this sense of emerging into an experience of heaven on earth through presence and growth :)
Looking forward to what you come up with!

```html
<!DOCTYPE html>
<html lang="en">
<head>
<meta charset="utf-8">
<title>Quiet Resolve — Book Cover</title>
<link rel="stylesheet" href="https://fonts.googleapis.com/css2?family=Cinzel:wght@400;500&family=Marcellus&display=swap">
<style>
  :root {
    --backdrop: #6e7982;
    --paper: #f3f4f5;
    --ink-slate: #39424c;
    --ink-red: #7a0f12;
    --mist-light: #f7f8f9;
    --mist-mid: #dfe3e6;
    --mist-deep: #c3c9ce;
    --foliage: 63,122,78;
  }
  html, body {
    margin: 0;
    padding: 0;
    width: 1200px;
    height: 1200px;
    overflow: hidden;
    background: var(--backdrop);
  }
  .canvas {
    position: relative;
    width: 1200px;
    height: 1200px;
    background: var(--backdrop);
  }
  .cover {
    position: absolute;
    left: 240px;
    top: 60px;
    width: 720px;
    height: 1080px;
    background: var(--paper);
    overflow: hidden;
    box-shadow: 0 10px 30px rgba(0,0,0,0.25);
  }
  .cover-art {
    position: absolute;
    left: 0;
    top: 480px;
    width: 720px;
    height: 600px;
    background:
      radial-gradient(ellipse 30% 20% at 50% 29%, rgba(var(--foliage),0.85) 0%, rgba(var(--foliage),0.6) 55%, rgba(var(--foliage),0) 100%),
      linear-gradient(180deg, var(--paper) 0%, var(--mist-light) 45%, var(--mist-mid) 72%, var(--mist-deep) 100%);
  }
  .title {
    position: absolute;
    left: 0;
    width: 100%;
    margin: 0;
    text-align: center;
    font-family: "Marcellus", serif;
    font-weight: 400;
    line-height: 1;
  }
  .title-quiet {
    top: 86px;
    font-size: 104px;
    color: var(--ink-slate);
    letter-spacing: -1px;
  }
  .title-resolve {
    top: 180px;
    font-size: 120px;
    color: var(--ink-red);
    letter-spacing: 1px;
  }
  .subtitle {
    position: absolute;
    top: 322px;
    left: 0;
    width: 100%;
    margin: 0;
    text-align: center;
    font-family: "Cinzel", serif;
    font-weight: 400;
    font-size: 24px;
    line-height: 40px;
    letter-spacing: 4px;
    color: var(--ink-slate);
  }
  .author {
    position: absolute;
    top: 950px;
    left: 0;
    width: 100%;
    margin: 0;
    text-align: center;
    font-family: "Cinzel", serif;
    font-weight: 500;
    font-size: 48px;
    line-height: 1;
    letter-spacing: 5px;
    color: var(--ink-slate);
  }
</style>
</head>
<body>
  <main class="canvas">
    <article class="cover">
      <div class="cover-art" role="img" aria-label="A lone leafy green tree rising out of a soft sea of white clouds, its roots faintly visible below"></div>
      <h1 class="title title-quiet">QUIET</h1>
      <h1 class="title title-resolve">RESOLVE</h1>
      <p class="subtitle">HOW TO WALK PAST DOUBT,<br>TRUST YOUR OWN VOICE,<br>AND KNOW YOUR WORTH</p>
      <p class="author">ROWAN ASHDALE</p>
    </article>
  </main>
</body>
</html>
```